Body therapist needs a business card

I need a card for my business which is teaching trainings in body therapy, the company is called Wellacombe Educational Group. I teach to massage therapists around Australia, South East Asia and the USA. I am attaching my logo which will guide you as to what colours I would like to have you consider. Please consult my website to find out more about what I do. www.kinetrova.com.au

My name is Gareth Wellacombe. My phone number is (03) 9157 2618 or 0412573086. email is info@kinetrova.com.au

```html
<!DOCTYPE html>
<html lang="en">
<head>
<meta charset="utf-8">
<title>Wellacombe Educational Group – Business Card</title>
<link href="https://fonts.googleapis.com/css2?family=Open+Sans:wght@400&family=Roboto:wght@400;700&display=swap" rel="stylesheet">
<style>
  :root {
    --brown: #5c3420;
    --red: #b01e2a;
    --green: #c8d92b;
    --paper: #ffffff;
    --backdrop: #e6e6e6;
    --ink: #4a2a1a;
  }
  * { box-sizing: border-box; margin: 0; padding: 0; }
  html, body { width: 1200px; height: 901px; overflow: hidden; }
  body { background: var(--backdrop); position: relative; font-family: "Roboto", sans-serif; }

  .card {
    position: absolute;
    width: 620px;
    height: 354px;
    background: var(--paper);
    box-shadow: 0 6px 18px rgba(0,0,0,0.18);
    overflow: hidden;
  }
  .card--front { left: 60px; top: 50px; }
  .card--back { left: 520px; top: 490px; }

  .band {
    position: absolute;
    left: 0; right: 0; bottom: 0;
    height: 18px;
    display: flex;
    gap: 4px;
  }
  .band__brown { background: var(--brown); }
  .band__red { background: var(--red); }
  .band__green { background: var(--green); }
  .card--front .band__brown { flex: 0 0 45%; }
  .card--front .band__red { flex: 0 0 30%; }
  .card--front .band__green { flex: 1; }
  .card--back .band__brown { flex: 0 0 43%; }
  .card--back .band__red { flex: 0 0 37%; }
  .card--back .band__green { flex: 1; }

  .brand {
    position: absolute;
    display: flex;
    align-items: center;
    font-family: "Open Sans", sans-serif;
    font-weight: 400;
    color: var(--brown);
  }
  .brand__dot { border-radius: 50%; background: var(--brown); flex: none; }
  .brand__name { line-height: 1.05; }
  .brand__name span { display: block; }

  .card--front .brand { left: 120px; top: 130px; gap: 22px; }
  .card--front .brand__dot { width: 72px; height: 72px; }
  .card--front .brand__name { font-size: 36px; }
  .card--front .brand__name span + span { font-size: 18px; margin-top: 4px; }

  .card--back .brand { right: 48px; top: 42px; gap: 14px; }
  .card--back .brand__dot { width: 44px; height: 44px; }
  .card--back .brand__name { font-size: 24px; }
  .card--back .brand__name span + span { font-size: 12px; margin-top: 3px; }

  .rule {
    position: absolute;
    height: 1px;
    background: var(--brown);
  }
  .rule--top { left: 300px; right: 40px; top: 130px; }
  .rule--name { left: 40px; width: 240px; top: 218px; }

  .holder {
    position: absolute;
    left: 40px; top: 190px;
    font-weight: 700;
    font-size: 22px;
    color: var(--red);
  }
  .contacts {
    position: absolute;
    left: 52px; top: 232px;
    list-style: none;
    font-size: 15px;
    color: var(--ink);
  }
  .contacts li { display: flex; align-items: center; gap: 10px; height: 24px; }
  .contacts svg { width: 14px; height: 14px; fill: var(--red); flex: none; }
  .address {
    position: absolute;
    right: 40px; top: 250px;
    font-size: 15px;
    line-height: 1.4;
    color: var(--ink);
  }
</style>
</head>
<body>

<section class="card card--front">
  <div class="brand">
    <div class="brand__dot"></div>
    <div class="brand__name"><span>Wellacombe</span><span>Educational Group</span></div>
  </div>
  <div class="band"><div class="band__brown"></div><div class="band__red"></div><div class="band__green"></div></div>
</section>

<section class="card card--back">
  <div class="brand">
    <div class="brand__dot"></div>
    <div class="brand__name"><span>Wellacombe</span><span>Educational Group</span></div>
  </div>
  <div class="rule rule--top"></div>
  <h1 class="holder">Gareth Wellacombe</h1>
  <div class="rule rule--name"></div>
  <ul class="contacts">
    <li><svg viewBox="0 0 24 24"><path d="M6.6 10.8a15 15 0 0 0 6.6 6.6l2.2-2.2c.3-.3.7-.4 1-.2 1.1.4 2.3.6 3.6.6.6 0 1 .4 1 1V20c0 .6-.4 1-1 1A17 17 0 0 1 3 4c0-.6.4-1 1-1h3.5c.6 0 1 .4 1 1 0 1.3.2 2.5.6 3.6.1.3 0 .7-.2 1z"/></svg>(03) 9157 2618</li>
    <li><svg viewBox="0 0 24 24"><path d="M2 5h20v14H2zm2 2v.5l8 5 8-5V7l-8 5z"/></svg>info@kinetrova.com.au</li>
    <li><svg viewBox="0 0 24 24"><path d="M12 2a10 10 0 1 0 0 20 10 10 0 0 0 0-20zm0 4a6 6 0 1 1 0 12 6 6 0 0 1 0-12z"/></svg>www.kinetrova.com.au</li>
  </ul>
  <address class="address">P.O. Box 2274, Ferntree Vale<br>Australia, Victoria, 3185</address>
  <div class="band"><div class="band__brown"></div><div class="band__red"></div><div class="band__green"></div></div>
</section>

</body>
</html>
```